Lumora Activewear business card design

I need a business card designed for my activewear business. I would like to use the colours pink, purple white and blue. please see attached logo. please include (name) Harriet Welloby (phone) 0417582064 (email) hattieslumora@mailvento.com (ABN) 48715290637 . please include - Free shipping on all orders over $100

Target Market(s)

female

Contact Information for Business Card

Colors

Requirements
Must have
• I need a business card designed for my activewear business. I would like to use the colours pink, purple white and blue. please see attached logo. please include (name) Harriet Welloby (phone) 0417582064 (email) hattieslumora@mailvento.com (ABN) 48715290637 . please include - Free shipping on all orders over $100

```html
<!DOCTYPE html>
<html lang="en">
<head>
<meta charset="utf-8">
<title>Lumora Activewear – Business Card</title>
<link href="https://fonts.googleapis.com/css2?family=Noto+Sans:wght@400;700&display=swap" rel="stylesheet">
<style>
  :root {
    --backdrop: #2a2a2c;
    --card-purple: #9e1bae;
    --wordmark: #dca6e6;
    --ink-white: #ffffff;
    --ornament-light: rgba(222, 150, 236, 0.45);
    --ornament-mid: rgba(190, 90, 210, 0.22);
    --ornament-clear: rgba(158, 27, 174, 0);
  }
  * { box-sizing: border-box; margin: 0; padding: 0; }
  html, body {
    width: 1200px;
    height: 900px;
    overflow: hidden;
    background: var(--backdrop);
    font-family: "Noto Sans", sans-serif;
  }
  .canvas {
    position: relative;
    width: 1200px;
    height: 900px;
  }
  .card {
    position: absolute;
    width: 600px;
    height: 340px;
    background: var(--card-purple);
    box-shadow: 0 14px 30px rgba(0, 0, 0, 0.55);
    overflow: hidden;
  }
  .card--front { left: 360px; top: 60px; }
  .card--back  { left: 200px; top: 490px; }

  .wordmark {
    position: absolute;
    left: 36px;
    top: 34px;
    font-size: 52px;
    font-weight: 700;
    letter-spacing: 4px;
    color: var(--wordmark);
    line-height: 1;
  }
  .heart-ornament {
    position: absolute;
    right: 6px;
    bottom: 6px;
    width: 250px;
    height: 210px;
    background: radial-gradient(closest-side, var(--ornament-light) 0%, var(--ornament-mid) 50%, var(--ornament-clear) 100%);
  }
  .contact {
    position: absolute;
    left: 36px;
    bottom: 30px;
    color: var(--ink-white);
    font-size: 17px;
    line-height: 1.5;
  }
  .contact__name {
    font-weight: 700;
    font-size: 19px;
    letter-spacing: 0.5px;
    margin-bottom: 6px;
  }
  .contact__line {
    display: flex;
    align-items: center;
    gap: 8px;
  }
  .contact__icon {
    width: 15px;
    height: 15px;
    fill: var(--ink-white);
    flex: none;
  }
  .contact__offer { margin-top: 4px; }
</style>
</head>
<body>
<main class="canvas">
  <section class="card card--front" aria-label="Business card front">
    <div class="wordmark">LUMORA</div>
    <div class="heart-ornament" role="img" aria-label="Embossed double heart outline decoration"></div>
  </section>

  <section class="card card--back" aria-label="Business card back">
    <div class="wordmark">LUMORA</div>
    <div class="heart-ornament" role="img" aria-label="Embossed double heart outline decoration"></div>
    <div class="contact">
      <p class="contact__name">HARRIET WELLOBY</p>
      <p class="contact__line">ABN 48715290637</p>
      <p class="contact__line">
        <svg class="contact__icon" viewBox="0 0 24 24" aria-hidden="true"><path d="M6.6 10.8a15.1 15.1 0 0 0 6.6 6.6l2.2-2.2a1 1 0 0 1 1-.25 11.4 11.4 0 0 0 3.6.57 1 1 0 0 1 1 1V20a1 1 0 0 1-1 1A17 17 0 0 1 3 4a1 1 0 0 1 1-1h3.5a1 1 0 0 1 1 1c0 1.25.2 2.46.57 3.6a1 1 0 0 1-.25 1z"/></svg>
        0417582064
      </p>
      <p class="contact__line">
        <svg class="contact__icon" viewBox="0 0 24 24" aria-hidden="true"><path d="M2 5h20v14H2z M2 5l10 8 10-8" fill="none" stroke="#fff" stroke-width="2"/></svg>
        hattieslumora@mailvento.com
      </p>
      <p class="contact__offer">Free shipping on all orders over $100</p>
    </div>
  </section>
</main>
</body>
</html>
```